Business Card Design

Selling beds and mattrices
See website www.lumirest.com.au for details
Targeting wholesale bed sellers

Industry/Entity Type

Business

Contact Information for Business Card

Lumirest
Director Gerald Pinwick
Beds and Mattrices - Most technologically advanced beds in the world
European designed and made
Already No 1 seller in Europe
Call now for a quote
ph: 0472 918 305
Email: sales@lumirest.com.au
www.lumirest.com.au

```html
<!DOCTYPE html>
<html lang="en">
<head>
<meta charset="utf-8">
<title>Lumirest Business Card</title>
<link rel="stylesheet" href="https://fonts.googleapis.com/css2?family=Ubuntu:wght@400;500;700&display=swap">
<style>
  :root {
    --page-bg: #e6e6e4;
    --card-white: #f7f7f5;
    --band-dark: #232323;
    --ink: #1c1c1c;
    --ink-soft: #6a6a6a;
    --accent-green: #8cc21e;
    --on-dark: #ffffff;
  }
  * { margin: 0; padding: 0; box-sizing: border-box; }
  html, body {
    width: 1200px; height: 1000px; overflow: hidden;
    background: var(--page-bg);
    font-family: "Ubuntu", sans-serif;
  }
  .business-card {
    position: absolute; left: 110px; top: 220px;
    width: 980px; height: 560px;
    background: var(--card-white);
    box-shadow: 0 8px 24px rgba(0,0,0,0.18);
    overflow: hidden;
  }
  .brand {
    position: absolute; left: 80px; top: 56px;
    display: flex; align-items: center; gap: 16px;
  }
  .brand-mark {
    width: 26px; height: 26px; border: 3px solid var(--ink);
  }
  .brand-name {
    font-size: 58px; font-weight: 400; letter-spacing: 4px;
    color: var(--ink); text-transform: uppercase;
  }
  .tagline {
    position: absolute; left: 80px; top: 176px; width: 700px;
    font-size: 19px; line-height: 1.3; color: var(--ink-soft);
    text-align: center;
  }
  .person {
    position: absolute; left: 650px; top: 118px;
  }
  .person-name { font-size: 28px; font-weight: 700; color: var(--ink); }
  .person-title { font-size: 16px; font-weight: 500; color: var(--ink); margin-top: 4px; }
  .contact-band {
    position: absolute; left: 0; top: 262px;
    width: 100%; height: 298px;
    background: var(--band-dark);
  }
  .call-to-action {
    position: absolute; left: 80px; top: 98px;
    font-size: 25px; color: var(--accent-green);
  }
  .contact-icons {
    position: absolute; left: 470px; top: 70px;
    display: flex; gap: 16px;
  }
  .contact-icon { width: 34px; height: 34px; }
  .contact-lines {
    position: absolute; left: 460px; top: 136px;
    font-size: 23px; line-height: 1.45; color: var(--on-dark);
  }
</style>
</head>
<body>
  <main class="business-card">
    <div class="brand">
      <span class="brand-mark"></span>
      <span class="brand-name">Lumirest</span>
    </div>
    <p class="tagline">Beds and Mattrices Most technologically advanced beds in the world European designed and made Already No 1 seller in Europe</p>
    <div class="person">
      <p class="person-name">Gerald Pinwick</p>
      <p class="person-title">Director</p>
    </div>
    <section class="contact-band">
      <p class="call-to-action">Call now for a quote</p>
      <div class="contact-icons">
        <svg class="contact-icon" viewBox="0 0 34 34" aria-label="Phone">
          <circle cx="17" cy="17" r="17" fill="#fff"/>
          <path d="M12 9c1 0 2 3 2 4s-1 1.5-1 2c0 1 3 5 5 5 .5 0 1-1 2-1s4 1 4 2-1 3-3 3c-5 0-11-7-11-12 0-2 1-3 2-3z" fill="var(--band-dark)"/>
        </svg>
        <svg class="contact-icon" viewBox="0 0 34 34" aria-label="Email">
          <circle cx="17" cy="17" r="17" fill="#fff"/>
          <rect x="9" y="11" width="16" height="12" fill="var(--band-dark)"/>
          <path d="M9 11l8 7 8-7" fill="none" stroke="#fff" stroke-width="1.5"/>
        </svg>
        <svg class="contact-icon" viewBox="0 0 34 34" aria-label="Website">
          <circle cx="17" cy="17" r="17" fill="#fff"/>
          <g fill="none" stroke="var(--band-dark)" stroke-width="1.8">
            <circle cx="17" cy="17" r="8"/>
            <ellipse cx="17" cy="17" rx="3.5" ry="8"/>
            <line x1="9" y1="17" x2="25" y2="17"/>
          </g>
        </svg>
      </div>
      <div class="contact-lines">
        <p class="contact-phone">ph: 0472 918 305</p>
        <p class="contact-email">Email: sales@lumirest.com.au</p>
        <p class="contact-web">www.lumirest.com.au</p>
      </div>
    </section>
  </main>
</body>
</html>
```